Mobile Spray tanner needs a Mobile Spray tanning business card design

I need a simple but eye-catching business card design. I would like the business card to be in two colours only (Hot pink background with black Silhouette & black writing). I would like the white behind the silhouette removed and the other bits on the silhouette removed (to be just a black silhouette with a hot pink bikini on). I would like the black writing to be aesthetically pleasing and quite artistic, but easy to read). Thank you very much

```html
<!DOCTYPE html>
<html lang="en">
<head>
<meta charset="utf-8">
<title>Golden Glowz – Business Card</title>
<link rel="stylesheet" href="https://fonts.googleapis.com/css2?family=Cinzel+Decorative:wght@700&family=Mulish:wght@300&family=Open+Sans:wght@700&display=swap">
<style>
  :root {
    --backdrop: #3b3631;
    --pink-deep: #d8106a;
    --pink-hot: #ec1e7c;
    --pink-light: #f0408e;
    --ink: #141012;
  }
  html, body {
    margin: 0;
    width: 1200px;
    height: 1024px;
    overflow: hidden;
    background: var(--backdrop);
  }
  .stage {
    width: 1200px;
    height: 1024px;
    display: flex;
    align-items: center;
    justify-content: center;
  }
  .card {
    position: relative;
    width: 520px;
    height: 910px;
    overflow: hidden;
    background: radial-gradient(ellipse at 60% 30%, var(--pink-light) 0%, var(--pink-hot) 45%, var(--pink-deep) 100%);
    box-shadow: 0 20px 50px rgba(0,0,0,0.45);
    color: var(--ink);
  }
  .silhouette {
    position: absolute;
    left: 130px;
    top: 150px;
    width: 280px;
    height: 380px;
    border-radius: 140px 140px 60px 60px;
    background: linear-gradient(180deg, #2a1a20 0%, var(--ink) 70%);
  }
  .brand {
    position: absolute;
    left: 50px;
    right: 40px;
    top: 580px;
  }
  .brand-name {
    margin: 0;
    font-family: "Cinzel Decorative", serif;
    font-weight: 700;
    font-size: 42px;
    letter-spacing: 0.5px;
    line-height: 1;
    white-space: nowrap;
  }
  .brand-tagline {
    margin: 10px 0 0 4px;
    font-family: "Mulish", sans-serif;
    font-weight: 300;
    font-size: 22px;
    letter-spacing: 1px;
    text-transform: uppercase;
  }
  .contact {
    position: absolute;
    left: 50px;
    top: 730px;
    display: flex;
    align-items: center;
    gap: 22px;
    font-family: "Open Sans", sans-serif;
    font-weight: 700;
    font-size: 34px;
    letter-spacing: 1px;
  }
  .contact svg {
    width: 30px;
    height: 30px;
    fill: var(--ink);
  }
</style>
</head>
<body>
  <main class="stage">
    <article class="card">
      <div class="silhouette" role="img" aria-label="Black silhouette of a kneeling woman wearing a hot pink bikini"></div>
      <header class="brand">
        <h1 class="brand-name">Golden Glowz</h1>
        <p class="brand-tagline">Mobile Spray Tanning</p>
      </header>
      <div class="contact">
        <svg viewBox="0 0 24 24" aria-hidden="true">
          <path d="M6.6 10.8c1.4 2.8 3.8 5.1 6.6 6.6l2.2-2.2c.3-.3.7-.4 1-.2 1.1.4 2.3.6 3.6.6.6 0 1 .4 1 1V20c0 .6-.4 1-1 1C10.6 21 3 13.4 3 4c0-.6.4-1 1-1h3.5c.6 0 1 .4 1 1 0 1.3.2 2.5.6 3.6.1.3 0 .7-.2 1l-2.3 2.2z"/>
        </svg>
        <span class="phone">555 210 0187</span>
      </div>
    </article>
  </main>
</body>
</html>
```